Bluebird Listings ad 2014 15

I need a design for an advertisement in our Bluebird Listings book telephone directory.
The directory runs for a 12 month period.

Our business offers 24 hour glass replacements to homes, shops and offices.
Our service is usually required by customers that require their glass replaced urgently
.
The ad is 1 of many in the directory offering the same service so we need to attract the customers attention quickly and easily and deliver our message - "24hr glass replacements to doors windows and shopfronts. Call now 9372 4816".

I want to keep the data in the attached ad but with a professional graphic presentation.

The ad size is 58mm high x 83mm wide, full colour.

Target Market(s)

Our customer is generally someone in need of an emergency repair. They aren't spending time shopping around for a product, they have a problem that they want fixed promptly and professionally.

Industry/Entity Type

Business

Font styles to use
Sans Serif

Colors
0255a3
f37022

Requirements
Must have
• "24HR" must stand out, this is a key aspect of our service. The ad needs to be clear and easy to read.

```html
<!DOCTYPE html>
<html lang="en">
<head>
<meta charset="utf-8">
<title>Steadfast Glass – 24hr Glass Replacement</title>
<link rel="stylesheet" href="https://fonts.googleapis.com/css2?family=Bebas+Neue&family=Oswald:wght@500;600&family=Open+Sans:wght@400&family=PT+Sans+Narrow:wght@400;700&family=Open+Sans+Condensed:wght@700&display=swap">
<style>
  :root {
    --brand-blue: #0255a3;
    --brand-orange: #f37022;
    --alert-red: #e2231f;
    --ink: #111111;
    --slate: #6b6b6b;
    --paper: #ffffff;
  }
  * { margin: 0; padding: 0; box-sizing: border-box; }
  html, body { width: 1200px; height: 839px; overflow: hidden; background: var(--paper); }
  .ad { position: relative; width: 1200px; height: 839px; background: var(--paper); overflow: hidden; }

  .brand-name {
    position: absolute; top: 6px; left: 0; width: 1200px; text-align: center;
    font-family: "Oswald", sans-serif; font-weight: 600; font-size: 92px; line-height: 100px;
    color: var(--brand-blue); letter-spacing: 2px; text-transform: uppercase;
  }
  .headline {
    position: absolute; top: 104px; left: 40px; width: 1150px;
    font-family: "Bebas Neue", sans-serif; font-size: 182px; line-height: 160px;
    color: var(--brand-blue); letter-spacing: 9px; white-space: nowrap;
  }
  .promise {
    position: absolute; top: 276px; left: 25px;
    font-family: "Bebas Neue", sans-serif; font-size: 80px; line-height: 72px;
    color: var(--ink); letter-spacing: 3px; -webkit-text-stroke: 1.5px var(--ink);
  }
  .call-line {
    position: absolute; top: 252px; left: 655px;
    font-family: "Oswald", sans-serif; font-weight: 500; font-size: 80px; line-height: 96px;
    color: var(--alert-red); letter-spacing: 1px; transform: scaleX(0.88); transform-origin: left;
    white-space: nowrap;
  }

  .service-panel { position: absolute; top: 379px; left: 0; width: 1200px; height: 383px; background: var(--brand-blue); }

  .checklist { position: absolute; top: 400px; left: 22px; list-style: none; }
  .checklist li {
    display: flex; align-items: center; height: 61.5px;
    font-family: "Open Sans", sans-serif; font-size: 31px; color: var(--paper); letter-spacing: 1px;
  }
  .checklist svg { width: 44px; height: 44px; margin-right: 12px; flex: none; }

  .insurance-note {
    position: absolute; top: 711px; left: 0; width: 361px; height: 47px; background: var(--paper);
    font-family: "PT Sans Narrow", sans-serif; font-size: 30px; line-height: 47px;
    color: var(--brand-blue); padding-left: 20px; letter-spacing: 1px;
  }

  .badge {
    position: absolute; left: 447px; width: 201px; background: var(--paper);
    text-align: center; font-family: "Oswald", sans-serif; font-weight: 500;
  }
  .badge-hours {
    top: 364px; height: 116px; border: 3px solid var(--brand-blue); border-radius: 4px;
    color: var(--alert-red); font-family: "Open Sans Condensed", sans-serif; font-weight: 700;
    line-height: 110px; white-space: nowrap;
  }
  .badge-hours .num { font-size: 82px; }
  .badge-hours .unit { font-size: 46px; letter-spacing: 4px; }
  .badge-guarantee {
    top: 494px; height: 114px; color: var(--brand-orange);
    font-size: 37px; line-height: 42px; padding-top: 14px; transform-origin: center;
  }
  .badge-trades {
    top: 628px; height: 114px; color: var(--brand-blue);
    font-size: 40px; line-height: 46px; padding-top: 10px;
  }
  .condensed { display: inline-block; transform: scaleX(0.82); }

  .message-box {
    position: absolute; top: 407px; left: 718px; width: 405px; height: 206px; background: var(--paper);
    padding: 18px 0 0 9px; font-family: "PT Sans Narrow", sans-serif; color: var(--brand-blue);
    font-size: 37px; line-height: 60px;
  }
  .message-box .accent { color: var(--alert-red); }
  .message-box .cta { font-family: "Open Sans", sans-serif; font-weight: 700; font-size: 35px; letter-spacing: 1px; }

  .trust-box {
    position: absolute; top: 622px; left: 722px; width: 404px; height: 128px;
    background: var(--slate); border: 4px solid var(--paper); border-radius: 3px;
    text-align: center; font-family: "Oswald", sans-serif; font-weight: 500;
    color: var(--paper); font-size: 40px; line-height: 50px; padding-top: 10px; letter-spacing: 1px;
  }

  .footer-band {
    position: absolute; top: 762px; left: 0; width: 1200px; height: 77px; background: var(--brand-orange);
    text-align: center; font-family: "Oswald", sans-serif; font-weight: 500;
    color: var(--paper); font-size: 35px; line-height: 77px; letter-spacing: 1.5px; white-space: nowrap;
  }
</style>
</head>
<body>
<main class="ad">
  <div class="brand-name">Steadfast Glass</div>
  <h1 class="headline">BROKEN GLASS?</h1>
  <p class="promise">WE CAN REPLACE IT</p>
  <p class="call-line">CALL 9372 4816</p>

  <section class="service-panel" aria-hidden="true"></section>

  <ul class="checklist">
    <li><svg viewBox="0 0 44 44"><rect x="3" y="9" width="32" height="32" fill="none" stroke="var(--brand-orange)" stroke-width="4"/><path d="M10 24 L18 33 L40 3" fill="none" stroke="#ffffff" stroke-width="4" stroke-linecap="round" stroke-linejoin="round"/></svg>DOOR GLASS</li>
    <li><svg viewBox="0 0 44 44"><rect x="3" y="9" width="32" height="32" fill="none" stroke="var(--brand-orange)" stroke-width="4"/><path d="M10 24 L18 33 L40 3" fill="none" stroke="#ffffff" stroke-width="4" stroke-linecap="round" stroke-linejoin="round"/></svg>WINDOW GLASS</li>
    <li><svg viewBox="0 0 44 44"><rect x="3" y="9" width="32" height="32" fill="none" stroke="var(--brand-orange)" stroke-width="4"/><path d="M10 24 L18 33 L40 3" fill="none" stroke="#ffffff" stroke-width="4" stroke-linecap="round" stroke-linejoin="round"/></svg>SHOWER GLASS</li>
    <li><svg viewBox="0 0 44 44"><rect x="3" y="9" width="32" height="32" fill="none" stroke="var(--brand-orange)" stroke-width="4"/><path d="M10 24 L18 33 L40 3" fill="none" stroke="#ffffff" stroke-width="4" stroke-linecap="round" stroke-linejoin="round"/></svg>SHOPFRONT</li>
    <li><svg viewBox="0 0 44 44"><rect x="3" y="9" width="32" height="32" fill="none" stroke="var(--brand-orange)" stroke-width="4"/><path d="M10 24 L18 33 L40 3" fill="none" stroke="#ffffff" stroke-width="4" stroke-linecap="round" stroke-linejoin="round"/></svg>STEADFAST GLASS</li>
  </ul>
  <p class="insurance-note">INSURANCE BILLED DIRECT</p>

  <div class="badge badge-hours"><span class="num">24</span><span class="unit">HR</span></div>
  <div class="badge badge-guarantee"><span class="condensed">ALL WORK<br>GUARANTEED</span></div>
  <div class="badge badge-trades"><span class="condensed">QUALIFIED<br>TRADESMEN</span></div>

  <div class="message-box">
    <span class="accent">24hr</span> glass replacements to<br>
    doors windows and shopfronts.<br>
    <span class="cta">Call now 9372 4816</span>.
  </div>
  <div class="trust-box"><span class="condensed">THE TRUSTED NAME IN<br>GLASS REPLACEMENT</span></div>

  <footer class="footer-band"><span class="condensed">REGAIN THE SAFETY AND SECURITY IN YOUR HOME, SHOP OR OFFICE</span></footer>
</main>
</body>
</html>
```